CareVantRx business cards

We need a business card design that we could customize as needed for employees. We will need space for Name, Title, 1-2 phone numbers and email address.

We are a Pharmacy Benefits Management (PBM) company for hospice agencies and beginning a nationwide expansion. Attached is a vector file of our logo.

Cards can be single or double sided.

Industry/Entity Type

Business

```html
<!DOCTYPE html>
<html lang="en">
<head>
<meta charset="utf-8">
<title>CareVantRx Business Cards</title>
<link rel="stylesheet" href="https://fonts.googleapis.com/css2?family=Questrial&display=swap">
<style>
  :root {
    --page: #ecebe8;
    --card: #ffffff;
    --green: #8fac5e;
    --green-soft: #b9c99a;
    --blue: #3a8fbf;
    --blue-soft: #b6d4e6;
    --ink: #3c3c3c;
    --muted: #7b7b7b;
    --faint: #eef1ea;
  }
  html, body {
    margin: 0;
    width: 1171px;
    height: 1200px;
    overflow: hidden;
    background: var(--page);
    font-family: "Questrial", "Century Gothic", sans-serif;
  }
  .sheet {
    width: 1171px;
    height: 1200px;
    display: flex;
    flex-direction: column;
    align-items: center;
    justify-content: center;
    gap: 40px;
  }
  .card {
    position: relative;
    width: 980px;
    height: 560px;
    background: var(--card);
    border-radius: 28px;
    overflow: hidden;
    box-shadow: 0 6px 24px rgba(0,0,0,0.12);
  }

  /* Front */
  .front .brand {
    position: absolute;
    left: 90px;
    top: 190px;
    display: flex;
    align-items: center;
    gap: 26px;
  }
  .brand-square {
    width: 92px;
    height: 92px;
    border-radius: 14px;
    background: var(--blue);
  }
  .brand-name {
    font-size: 96px;
    color: var(--blue);
    letter-spacing: -1px;
    line-height: 1;
  }
  .front .tagline {
    position: absolute;
    left: 208px;
    top: 318px;
    font-size: 25px;
    letter-spacing: 5px;
    color: var(--ink);
  }
  .front .corner-mark {
    position: absolute;
    right: 70px;
    top: 50px;
    width: 120px;
    height: 120px;
    border-radius: 18px;
    background: var(--faint);
  }
  .edge-band {
    position: absolute;
    left: 0;
    bottom: 0;
    width: 100%;
    height: 44px;
  }

  /* Back */
  .back .contact-bar {
    position: absolute;
    left: 0;
    top: 0;
    width: 100%;
    height: 96px;
    background: var(--green);
    display: flex;
    align-items: center;
    gap: 34px;
    padding-left: 70px;
    box-sizing: border-box;
  }
  .contact-bar svg { width: 34px; height: 34px; }
  .back .contact-list {
    position: absolute;
    left: 70px;
    top: 140px;
    font-size: 24px;
    line-height: 1.7;
    color: var(--ink);
  }
  .back .person {
    position: absolute;
    left: 70px;
    bottom: 90px;
  }
  .person-name {
    font-size: 46px;
    letter-spacing: 2px;
    color: var(--green);
  }
  .person-title {
    font-size: 22px;
    letter-spacing: 4px;
    color: var(--muted);
    margin-top: 6px;
  }
  .back .brand-small {
    position: absolute;
    right: 70px;
    bottom: 100px;
    display: flex;
    align-items: center;
    gap: 14px;
  }
  .brand-small .brand-square { width: 48px; height: 48px; border-radius: 8px; }
  .brand-small .brand-name { font-size: 50px; }
</style>
</head>
<body>
<main class="sheet">

  <section class="card front" aria-label="Card front">
    <div class="corner-mark"></div>
    <div class="brand">
      <div class="brand-square"></div>
      <div class="brand-name">CareVantRx</div>
    </div>
    <div class="tagline">PHARMACY BENEFITS MANAGEMENT</div>
    <svg class="edge-band" viewBox="0 0 980 44" preserveAspectRatio="none" aria-hidden="true">
      <rect x="0" y="14" width="980" height="30" fill="var(--green)"/>
      <path d="M640 44 L640 24 Q640 4 670 4 L980 4 L980 44 Z" fill="var(--blue)"/>
    </svg>
  </section>

  <section class="card back" aria-label="Card back">
    <div class="contact-bar">
      <svg viewBox="0 0 24 24" aria-label="Location"><path d="M12 2a7 7 0 0 0-7 7c0 5 7 13 7 13s7-8 7-13a7 7 0 0 0-7-7zm0 9.5A2.5 2.5 0 1 1 12 6.5a2.5 2.5 0 0 1 0 5z" fill="#fff"/></svg>
      <svg viewBox="0 0 24 24" aria-label="Email"><rect x="2" y="5" width="20" height="14" rx="2" fill="#fff"/><path d="M3 6l9 7 9-7" fill="none" stroke="var(--green)" stroke-width="1.6"/></svg>
      <svg viewBox="0 0 24 24" aria-label="Phone"><rect x="7" y="2" width="10" height="20" rx="2" fill="#fff"/><rect x="9" y="5" width="6" height="11" fill="var(--green)"/></svg>
      <svg viewBox="0 0 24 24" aria-label="Fax"><rect x="3" y="8" width="18" height="11" rx="2" fill="#fff"/><rect x="7" y="3" width="10" height="6" fill="#fff"/></svg>
    </div>
    <div class="contact-list">
      <div>Your Street Address</div>
      <div>City, State 00000</div>
      <div>name@carevantrx.com</div>
      <div>555 010 2040</div>
    </div>
    <div class="person">
      <div class="person-name">NAME</div>
      <div class="person-title">DESIGNATION</div>
    </div>
    <div class="brand-small">
      <div class="brand-square"></div>
      <div class="brand-name">CareVantRx</div>
    </div>
    <svg class="edge-band" viewBox="0 0 980 44" preserveAspectRatio="none" aria-hidden="true">
      <rect x="0" y="14" width="980" height="30" fill="var(--green)"/>
      <path d="M640 44 L640 24 Q640 4 670 4 L980 4 L980 44 Z" fill="var(--blue)"/>
    </svg>
  </section>

</main>
</body>
</html>
```